Flyer for Photo booth business for wedding expo

Hi the flyer is for velvet lantern photo booth rentals.
We are wanting a flyer for a wedding expo this weekend.

1 sided A4

Check out our website for colours etc www.lanternsnapbox.com.au

We are offering 10% discount on Platinum Packages for bookings confirmed within two weeks of the Bridal expo.

Expo Engagement party and Wedding package $1,900.00

Savings of $320.00

3 hour photo booth hire for Engagement package with the funky retro party booth including Props and Logo.

4 hour Platinum Wedding package with Video messaging.

We have a logos and images for the brochure, we are looking for a sleek and fun design with the velvet lantern colours.

www.lanternsnapbox.com.au
info@lanternsnapbox.com.au
0417 263 518

Target Market(s)

potential bride and grooms. partys weddings

Industry/Entity Type

Wedding

Requirements
Must have
• logo and wedding feel
Nice to have
• inventive and creative layout

```html
<!DOCTYPE html>
<html lang="en">
<head>
<meta charset="utf-8">
<title>Velvet Lantern Photobooth – Bridal Expo Flyer</title>
<link rel="stylesheet" href="https://fonts.googleapis.com/css2?family=Mulish:wght@400;800;900&family=Questrial&display=swap">
<style>
:root{
  --violet-deep:#5a1fa8;
  --violet:#7a3fd0;
  --violet-soft:#b48ae8;
  --lilac:#e4d4fa;
  --ink:#111016;
  --grey:#6d6a74;
  --white:#ffffff;
  --dash:#8c6bb8;
}
*{margin:0;padding:0;box-sizing:border-box}
html,body{width:867px;height:1200px;overflow:hidden;background:var(--white)}
.flyer{
  position:relative;width:867px;height:1200px;overflow:hidden;
  background:
    radial-gradient(ellipse 58% 48% at 50% 56%, #ffffff 0%, #fbf7ff 45%, var(--lilac) 70%, var(--violet-soft) 88%, var(--violet) 100%);
  font-family:"Mulish",sans-serif;color:var(--ink);text-align:center;
}
.flyer::after{
  content:"";position:absolute;inset:0;pointer-events:none;
  box-shadow:inset 0 0 90px 30px rgba(90,31,168,.55);
}
.hero-image{
  position:absolute;left:0;top:0;width:867px;height:400px;
  background:
    radial-gradient(ellipse 30% 40% at 68% 22%, rgba(200,170,240,.9), transparent 70%),
    radial-gradient(ellipse 28% 26% at 22% 58%, rgba(235,230,245,.95), rgba(170,150,200,.5) 60%, transparent 80%),
    linear-gradient(180deg, #c9a8f0 0%, #e9dcfb 55%, rgba(255,255,255,0) 100%);
}
.photo{
  position:absolute;background:var(--white);padding:8px;
  box-shadow:0 0 0 3px rgba(122,63,208,.6),0 6px 18px rgba(60,20,110,.45);
}
.photo span{
  display:block;width:100%;height:100%;
  background:linear-gradient(140deg,#d8d2de 0%,#8f8898 55%,#4c4654 100%);
}
.brand{
  position:absolute;left:150px;top:410px;width:440px;
  font-family:"Questrial",sans-serif;color:var(--violet);
  font-size:52px;line-height:54px;text-align:center;letter-spacing:1px;
}
.brand-dot{
  position:absolute;left:612px;top:420px;width:96px;height:96px;border-radius:50%;
  background:var(--violet-deep);
}
.copy{position:absolute;left:0;width:867px;font-size:22px;line-height:27px}
.copy b{font-weight:900}
.rule{position:absolute;left:118px;width:631px;border-top:2px dashed var(--dash)}
.contact{position:absolute;left:0;width:867px;font-size:21px;line-height:26px}
.contact b{font-weight:900;font-size:23px}
.web{
  position:absolute;left:0;top:1092px;width:867px;
  font-size:43px;font-weight:900;color:var(--violet-deep);letter-spacing:.5px;
}
</style>
</head>
<body>
<main class="flyer">
  <div class="hero-image" role="img" aria-label="Soft-focus wedding rings resting beside a bridal bouquet in lavender tones"></div>

  <div class="photo" style="left:478px;top:196px;width:128px;height:176px;transform:rotate(-3deg)">
    <span role="img" aria-label="Black and white photo booth strip of guests posing"></span></div>
  <div class="photo" style="left:596px;top:186px;width:124px;height:190px;transform:rotate(4deg)">
    <span role="img" aria-label="Black and white photo booth strip of friends posing"></span></div>

  <div class="brand">Velvet Lantern<br>Photobooth</div>
  <div class="brand-dot"></div>

  <p class="copy" style="top:538px"><b>10% discount on Platinum</b> Packages for bookings<br>confirmed within two weeks of the Bridal expo.</p>
  <div class="rule" style="top:598px"></div>
  <p class="copy" style="top:608px">Expo Engagement party and Wedding <b>package $1,900.00</b><br><b>Savings of $320.00</b></p>
  <div class="rule" style="top:668px"></div>

  <div class="photo" style="left:148px;top:690px;width:148px;height:188px;transform:rotate(-4deg)">
    <span role="img" aria-label="Guests in formal wear at a photo booth"></span></div>
  <div class="photo" style="left:298px;top:678px;width:150px;height:180px;transform:rotate(3deg)">
    <span role="img" aria-label="Bride laughing with guests wearing party props"></span></div>
  <div class="photo" style="left:450px;top:694px;width:146px;height:190px;transform:rotate(-2deg)">
    <span role="img" aria-label="Guest posing with novelty shutter glasses"></span></div>
  <div class="photo" style="left:590px;top:682px;width:140px;height:184px;transform:rotate(5deg)">
    <span role="img" aria-label="Couple posing at a wedding photo booth"></span></div>

  <p class="copy" style="top:904px"><b>3 hour photo booth hire for Engagement package</b> with<br>the funky retro party booth including Props and Logo.</p>
  <div class="rule" style="top:962px"></div>
  <p class="copy" style="top:970px"><b>4 hour Platinum Wedding package</b> with Video messaging.</p>
  <div class="rule" style="top:1004px"></div>

  <p class="contact" style="top:1030px">Phone // <b>0417 263 518</b></p>
  <p class="contact" style="top:1058px">Email // <b>INFO@LANTERNSNAPBOX.COM.AU</b></p>
  <p class="web">www.lanternsnapbox.com.au</p>
</main>
</body>
</html>
```